Solar appointment reminder card

We are looking for a new design for our appointment reminder card since we have changed our logo. The card should have the new logo along with space for the employee to hand write the customers appointment date, time, the employees name and phone number.
I've uploaded what our old basic appointment card looked like and our new logo.

The cards should be in a standard business card size and could be horizontal or vertical.

```html
<!DOCTYPE html>
<html lang="en">
<head>
<meta charset="utf-8">
<title>Appointment Reminder Card</title>
<link rel="stylesheet" href="https://fonts.googleapis.com/css2?family=Arimo:wght@700&display=swap">
<style>
  :root {
    --paper: #ffffff;
    --orange: #f39325;
    --orange-text: #f28a2a;
    --yellow: #fcc52b;
    --yellow-border: #fac232;
  }
  html, body {
    margin: 0;
    padding: 0;
    overflow: hidden;
    background: var(--paper);
  }
  .card {
    position: relative;
    width: 1200px;
    height: 686px;
    background: var(--paper);
    font-family: "Arimo", Arial, sans-serif;
    font-weight: 700;
    overflow: hidden;
  }
  .card-title {
    position: absolute;
    left: 636px;
    top: 29px;
    width: 514px;
    height: 107px;
    box-sizing: border-box;
    border: 3px solid var(--orange);
    border-radius: 3px;
    margin: 0;
    display: flex;
    align-items: center;
    justify-content: center;
    color: var(--yellow);
    font-size: 70px;
    font-weight: 700;
    line-height: 1;
  }
  .field-label {
    position: absolute;
    left: 58px;
    height: 84px;
    box-sizing: border-box;
    border: 3px solid var(--yellow-border);
    border-radius: 3px;
    padding-left: 24px;
    display: flex;
    align-items: center;
    color: var(--orange-text);
    font-size: 49px;
    line-height: 1;
  }
  .label-date { top: 176px; width: 190px; }
  .label-time { top: 293px; width: 190px; }
  .label-rep { top: 404px; width: 442px; }
  .label-phone { top: 523px; width: 234px; }
  .write-line {
    position: absolute;
    left: 638px;
    width: 500px;
    height: 3px;
    background: var(--orange);
  }
  .line-date { top: 257px; }
  .line-time { top: 374px; }
  .line-rep { top: 485px; }
  .line-phone { top: 604px; }
</style>
</head>
<body>
  <main class="card">
    <h1 class="card-title">Appointment</h1>

    <div class="field-label label-date">Date:</div>
    <div class="write-line line-date"></div>

    <div class="field-label label-time">Time:</div>
    <div class="write-line line-time"></div>

    <div class="field-label label-rep">Representative:</div>
    <div class="write-line line-rep"></div>

    <div class="field-label label-phone">Phone:</div>
    <div class="write-line line-phone"></div>
  </main>
</body>
</html>
```